Employee Benefits and Insurance Consulting

We are an existing company with over 30 years experience but are changing our name. We would like a simple design with grey tones.

Industry/Entity Type

Insurance

Contact Information for Business Card

Crestwell Benefits Consulting
Gregory L Marsh CEO
5172 Pembrook Road
Louisville, TN 37777
greg@crestwellbc-example.com
865-412-3956 - O
865-547-2081 - C

```html
<!DOCTYPE html>
<html lang="en">
<head>
<meta charset="utf-8">
<title>Crestwell Benefits Consulting – Business Card</title>
<link href="https://fonts.googleapis.com/css2?family=Open+Sans:wght@400;600;700&display=swap" rel="stylesheet">
<style>
  :root {
    --teal: #1f9389;
    --teal-dark: #17776f;
    --grey: #6b6b6b;
    --grey-light: #cfcfcf;
    --white: #ffffff;
    --paper: #f7f7f7;
    --backdrop: #e9e9e9;
    --shadow: rgba(0, 0, 0, 0.18);
  }
  * { margin: 0; padding: 0; box-sizing: border-box; }
  html, body {
    width: 1200px; height: 900px; overflow: hidden;
    background: var(--backdrop);
    font-family: "Open Sans", Arial, sans-serif;
  }
  .stage {
    position: relative; width: 1200px; height: 900px;
    display: flex; align-items: center; justify-content: center; gap: 40px;
  }
  .card {
    position: relative; width: 520px; height: 297px;
    border-radius: 3px; overflow: hidden;
    box-shadow: 0 10px 24px var(--shadow);
  }

  /* Front */
  .card-front {
    background: var(--teal);
    display: flex; align-items: center; justify-content: center;
  }
  .brand-name {
    color: var(--white); font-weight: 600; text-align: center;
    font-size: 26px; letter-spacing: 3px; line-height: 1.35;
    text-transform: uppercase;
  }

  /* Back */
  .card-back { background: var(--teal); }
  .back-top {
    position: absolute; left: 0; top: 0; width: 100%; height: 168px;
    background: linear-gradient(180deg, var(--white), var(--paper));
    display: flex; align-items: center; justify-content: center;
  }
  .back-top .brand-name { color: var(--teal); font-size: 24px; }
  .back-rule {
    position: absolute; left: 0; top: 168px; width: 100%; height: 9px;
    background: var(--grey);
  }
  .back-bottom {
    position: absolute; left: 0; top: 177px; width: 100%; height: 120px;
    display: flex; align-items: center; justify-content: space-between;
    padding: 0 34px 0 44px; color: var(--white);
  }
  .holder { text-align: right; }
  .holder-name { font-size: 19px; font-weight: 700; }
  .holder-role { font-size: 13px; font-weight: 700; }
  .holder-address { font-size: 14px; line-height: 1.35; margin-top: 4px; }
  .contact-list { list-style: none; font-size: 12.5px; line-height: 1.9; }
  .contact-list li { display: flex; align-items: center; gap: 9px; }
  .contact-list svg { width: 12px; height: 12px; fill: var(--white); flex: none; }
</style>
</head>
<body>
<main class="stage">
  <section class="card card-front" aria-label="Card front">
    <p class="brand-name">Crestwell Benefits<br>Consulting</p>
  </section>

  <section class="card card-back" aria-label="Card back">
    <div class="back-top">
      <p class="brand-name">Crestwell Benefits<br>Consulting</p>
    </div>
    <div class="back-rule"></div>
    <div class="back-bottom">
      <div class="holder">
        <p><span class="holder-name">Gregory L Marsh</span> <span class="holder-role">- CEO</span></p>
        <p class="holder-address">5172 Pembrook Road<br>Louisville, TN 37777</p>
      </div>
      <ul class="contact-list">
        <li>
          <svg viewBox="0 0 24 24" aria-hidden="true"><path d="M6.6 10.8a15.1 15.1 0 0 0 6.6 6.6l2.2-2.2c.3-.3.7-.4 1-.2 1.1.4 2.3.6 3.6.6.6 0 1 .4 1 1V20c0 .6-.4 1-1 1C10.6 21 3 13.4 3 4c0-.6.4-1 1-1h3.5c.6 0 1 .4 1 1 0 1.3.2 2.5.6 3.6.1.3 0 .7-.2 1z"/></svg>
          865-547-2081
        </li>
        <li>
          <svg viewBox="0 0 24 24" aria-hidden="true"><path d="M7 1h10a2 2 0 0 1 2 2v18a2 2 0 0 1-2 2H7a2 2 0 0 1-2-2V3a2 2 0 0 1 2-2zm0 3v14h10V4zm5 15.5a1.2 1.2 0 1 0 0 2.4 1.2 1.2 0 0 0 0-2.4z"/></svg>
          865-412-3956
        </li>
        <li>
          <svg viewBox="0 0 24 24" aria-hidden="true"><path d="M2 5h20v14H2zm2 2v.5l8 5 8-5V7zm0 2.8V17h16V9.8l-8 5z"/></svg>
          greg@crestwellbc-example.com
        </li>
      </ul>
    </div>
  </section>
</main>
</body>
</html>
```